Design of business signage for outside store front

We need signage designed for outside a store front.  We already have a logo, colours and font that we would like to use but would like some ideas as regards layout/design of the signage.  The final product will be for the use of the installer to produce and install the signage.  Attached are files with our logo and font and a picture of the current signage which needs to be replaced.  The size and shape of the signage will be the same as the current signage, its just the design/layout that we would like changed.
N.B. We would like two versions if possible, one with the web address and one without the web address to see what they look like.

```html
<!DOCTYPE html>
<html lang="en">
<head>
<meta charset="utf-8">
<title>Relish Iberia – Storefront Signage</title>
<link rel="stylesheet" href="https://fonts.googleapis.com/css2?family=Cardo&family=Arimo:wght@400;700&display=swap">
<style>
  :root {
    --maroon: #8b2833;
    --gold: #f2d035;
    --gold-soft: #f8e7a6;
    --cream: #fbf4e4;
    --white: #ffffff;
    --page: #ffffff;
  }
  html, body {
    margin: 0;
    padding: 0;
    width: 825px;
    height: 1200px;
    overflow: hidden;
    background: var(--page);
  }
  .canvas {
    position: relative;
    width: 825px;
    height: 1200px;
  }
  .sign {
    position: absolute;
    left: 71px;
    width: 684px;
    height: 284px;
    display: block;
    filter: drop-shadow(0 4px 10px rgba(0,0,0,0.12));
  }
  .sign--plain { top: 285px; }
  .sign--web { top: 606px; }
  .ground-stop--left { stop-color: var(--gold-soft); }
  .ground-stop--mid { stop-color: var(--white); }
  .ground-stop--right { stop-color: var(--cream); }
  .emblem { fill: var(--maroon); }
  .name { font-family: "Cardo", "Times New Roman", serif; }
  .name__main { font-size: 104px; fill: var(--maroon); }
  .name__sub { font-size: 68px; fill: var(--gold); }
  .tagline__bar { fill: var(--maroon); }
  .tagline__text {
    font-family: "Arimo", Arial, sans-serif;
    font-size: 23px;
    fill: var(--white);
  }
  .web {
    font-family: "Arimo", Arial, sans-serif;
    font-weight: 700;
    font-size: 21px;
    fill: var(--gold);
  }
  .web__domain { fill: var(--maroon); }
</style>
</head>
<body>
<main class="canvas">

  <svg width="0" height="0" aria-hidden="true" style="position:absolute">
    <defs>
      <linearGradient id="sign-ground" x1="0" y1="0" x2="1" y2="1">
        <stop class="ground-stop--left" offset="0"/>
        <stop class="ground-stop--mid" offset="0.35"/>
        <stop class="ground-stop--mid" offset="0.6"/>
        <stop class="ground-stop--right" offset="1"/>
      </linearGradient>
    </defs>
  </svg>

  <!-- Version without web address -->
  <svg class="sign sign--plain" viewBox="0 0 684 284" aria-label="Relish Iberia storefront sign">
    <rect width="684" height="284" fill="url(#sign-ground)" role="img" aria-label="Background decoration of scattered gold, maroon and cream circles"/>
    <rect class="emblem" x="22" y="34" width="143" height="216" role="img" aria-label="Brand emblem area: dancer silhouette with golden ribbon"/>
    <text class="name name__main" x="195" y="121" textLength="442" lengthAdjust="spacingAndGlyphs">RELISH</text>
    <text class="name name__sub" x="195" y="190" textLength="442" lengthAdjust="spacing">IBERIA</text>
    <rect class="tagline__bar" x="192" y="206" width="446" height="37"/>
    <text class="tagline__text" x="200" y="233" textLength="430" lengthAdjust="spacing">Spanish Artisan Foods</text>
  </svg>

  <!-- Version with web address -->
  <svg class="sign sign--web" viewBox="0 0 684 284" aria-label="Relish Iberia storefront sign with web address">
    <rect width="684" height="284" fill="url(#sign-ground)" role="img" aria-label="Background decoration of scattered gold, maroon and cream circles"/>
    <rect class="emblem" x="22" y="34" width="143" height="216" role="img" aria-label="Brand emblem area: dancer silhouette with golden ribbon"/>
    <text class="name name__main" x="195" y="112" textLength="442" lengthAdjust="spacingAndGlyphs">RELISH</text>
    <text class="name name__sub" x="195" y="172" textLength="442" lengthAdjust="spacing">IBERIA</text>
    <rect class="tagline__bar" x="192" y="182" width="446" height="36"/>
    <text class="tagline__text" x="200" y="208" textLength="430" lengthAdjust="spacing">Spanish Artisan Foods</text>
    <text class="web" x="196" y="248" textLength="441" lengthAdjust="spacing">www.<tspan class="web__domain">relishiberia</tspan>.com.au</text>
  </svg>

</main>
</body>
</html>
```